Text only wordpress site to capture emails

Refer to inspiration upload for list of sites that will be useful for you.

We need a site that will be used to capture emails from clients that follow us on social media. The site will be all text, pretty simple. I have a couple of text sites that I like and we can use them for an example.

Menu section will have home, archive, about.
Footer will have © and Website Privacy Policy | Legal and Policies
There will be some text on the home page and an email capture.

This site will be all text no pictures.

I discuss office politics so the text portions will have some questions and answers on this and then prompt for the visitor to subscribe to my email list.

The only purpose of the site is to build an email list from existing social media followers so the site will be pretty simple in and of itself.

• Text only, similar Q&A to uploaded pics.

I will use a template from letter pinecone dotcom for email capture.

I like the simple couriernew font family that is on both sites supplied in the uploads.
• If you use any color it needs to be very minimal.

```html
<!DOCTYPE html>
<html lang="en">
<head>
<meta charset="utf-8">
<title>Office Politics Q&amp;A</title>
<link href="https://fonts.googleapis.com/css2?family=Courier+Prime:wght@400;700&family=Roboto:wght@300;400;500;700&family=Raleway:wght@400;500&display=swap" rel="stylesheet">
<style>
:root{
  --ink:#3a4250;
  --ink-soft:#5d6470;
  --muted:#8c929b;
  --accent:#4ea6e8;
  --accent-btn:#5cb0ec;
  --line:#e2e5ea;
  --tint:#f8f9fd;
  --tint-2:#f8f9fb;
  --arrow:#9aa0a8;
  --white:#ffffff;
}
*{margin:0;padding:0;box-sizing:border-box}
html,body{width:1200px;height:2713px;overflow:hidden;background:var(--white);color:var(--ink)}
body{position:relative;font-family:"Courier New","Courier Prime",monospace}
.abs{position:absolute}

/* header */
.site-header{left:0;top:0;width:1200px;height:77px;border-bottom:1px solid #eceef2;background:var(--tint)}
.brand{left:148px;top:24px;font-family:"Raleway",sans-serif;font-size:21px;font-weight:500;letter-spacing:.3px;color:var(--ink)}
.nav a{position:absolute;font-family:"Raleway",sans-serif;font-size:16px;color:var(--ink);text-decoration:none}
.nav .current{left:743px;top:19px;width:96px;height:36px;border:1.5px solid var(--accent);border-radius:2px;line-height:33px;text-align:center;box-shadow:0 6px 12px rgba(80,100,140,.12);background:var(--white)}
.nav .archive{left:890px;top:27px}
.nav .about{left:1004px;top:27px}

/* hero */
.hero{left:0;top:78px;width:1200px;height:581px;background:var(--tint)}
.hero-title{left:0;top:186px;width:1200px;text-align:center;font-family:"Roboto",sans-serif;font-size:38px;line-height:51px;font-weight:300;color:var(--ink)}
.hero-title b{font-weight:700}
.hero-lede{left:0;top:311px;width:1200px;text-align:center;font-size:15.5px;line-height:29px;color:var(--ink-soft)}
.signup{width:472px;height:50px;background:var(--white);box-shadow:0 10px 20px rgba(60,70,90,.10);border:1px solid #eef0f3}
.signup .field{position:absolute;left:22px;top:15px;font-size:15.5px;color:var(--ink-soft)}
.signup .btn{position:absolute;right:5px;top:5px;width:124px;height:38px;background:var(--accent-btn);color:var(--white);font-size:15.5px;font-weight:700;line-height:38px;text-align:center}

/* faq */
.faq-title{left:148px;top:716px;font-family:"Roboto",sans-serif;font-size:27px;font-weight:500;color:var(--ink)}
.faq-row{left:152px;width:897px;border-bottom:1px solid var(--line)}
.faq-q{position:absolute;left:4px;font-size:15.5px;color:var(--ink)}
.faq-row.open{border-bottom:1.5px solid var(--accent)}
.faq-row.open .faq-q{color:var(--accent);font-weight:700}
.faq-icon{position:absolute;left:848px}
.faq-answer{left:174px;top:929px;width:824px;font-size:14px;line-height:22.5px;color:var(--ink-soft)}

/* blog */
.blog{left:0;top:1521px;width:1200px;height:1032px;background:var(--tint-2)}
.blog-title{left:148px;top:1580px;font-family:"Roboto",sans-serif;font-size:32px;font-weight:300;color:var(--ink)}
.blog-title b{font-weight:500}
.search{left:806px;top:1581px;width:243px;height:35px;background:#eff1f4;border-radius:3px}
.search span{position:absolute;left:18px;top:9px;font-family:"Roboto",sans-serif;font-size:13.5px;color:var(--ink)}
.search svg{position:absolute;right:18px;top:13px}
.blog-rule{left:150px;top:1643px;width:899px;height:1px;background:var(--line)}
.card{width:282px;height:280px;background:var(--white);border:1px solid #e6e8ec;border-radius:3px}
.card.lift{box-shadow:0 10px 22px rgba(60,70,90,.13)}
.card .tag{position:absolute;left:28px;top:30px;font-size:11.5px;color:var(--muted)}
.card h3{position:absolute;left:28px;top:53px;width:230px;font-weight:400;font-size:17px;line-height:22.5px;color:var(--ink)}
.card p{position:absolute;left:28px;top:112px;width:224px;font-size:12.6px;line-height:21px;color:var(--ink-soft)}
.card .go{position:absolute;right:-1px;bottom:-1px;width:37px;height:37px;background:var(--arrow)}
.card.lift .go{background:var(--accent-btn)}
.card .go svg{position:absolute;left:11px;top:11px}
.more{left:539px;top:2350px;width:123px;height:40px;background:var(--accent-btn);color:var(--white);font-size:15.5px;line-height:40px;text-align:center}

/* footer */
.footer-nav a{position:absolute;top:2581px;font-family:"Raleway",sans-serif;font-size:16px;color:var(--ink);text-decoration:none}
.social{top:2580px}
.footer-rule{left:148px;top:2628px;width:901px;height:1px;background:var(--line)}
.copy{left:148px;top:2652px;font-size:14px;color:var(--ink)}
.legal{top:2652px;font-size:14px;color:var(--ink)}
.legal a{color:var(--ink);text-decoration:underline;text-underline-offset:3px}
</style>
</head>
<body>

<header class="abs site-header">
  <div class="abs brand">OFFICE NOTES</div>
  <nav class="nav">
    <a class="current" href="#">Home</a>
    <a class="archive" href="#">Archive</a>
    <a class="about" href="#">About</a>
  </nav>
</header>

<section class="abs hero"></section>
<h1 class="abs hero-title">Lorem Ipsum is <b>Simply Dummy</b><br><b>Text of the Printing</b></h1>
<p class="abs hero-lede">Lorem Ipsum is simply dummy text of the printing and typesetting<br>industry. Lorem Ipsum has been the industry's.</p>
<div class="abs signup" style="left:364px;top:421px">
  <span class="field">Your Email Address</span>
  <span class="btn">Subscribe</span>
</div>

<h2 class="abs faq-title">Frequently Asked Questions</h2>

<div class="abs faq-row" style="top:790px;height:59px"><span class="faq-q" style="top:19px">Lorem Ipsum is simply dummy text ?</span>
  <svg class="faq-icon" style="top:16px" width="30" height="30" viewBox="0 0 30 30"><circle cx="15" cy="15" r="13" fill="none" stroke="#a8adb4" stroke-width="1.3"/><path d="M15 8v14M8 15h14" stroke="#a8adb4" stroke-width="1.3"/></svg></div>
<div class="abs faq-row open" style="top:849px;height:57px"><span class="faq-q" style="top:18px">Lorem Ipsum is simply dummy text of the printing ?</span>
  <svg class="faq-icon" style="top:13px" width="30" height="30" viewBox="0 0 30 30"><circle cx="15" cy="15" r="13" fill="none" stroke="#4ea6e8" stroke-width="1.5"/><path d="M8 15h14" stroke="#4ea6e8" stroke-width="1.5"/></svg></div>
<p class="abs faq-answer">Lorem Ipsum is simply dummy text of the printing and typesetting industry. Lorem Ipsum has been the industry's standard dummy text ever since the 1500s, when an unknown printer took a galley of type and scrambled it to make a type specimen book. It has survived not only five centuries, but also the leap into electronic typesetting, remaining essentially unchanged. It has survived not only five centuries, but</p>
<div class="abs faq-row" style="top:1076px;height:1px"></div>
<div class="abs faq-row" style="top:1077px;height:59px"><span class="faq-q" style="top:20px">Lorem Ipsum is simply dummy text of the printing and typesetting ?</span>
  <svg class="faq-icon" style="top:15px" width="30" height="30" viewBox="0 0 30 30"><circle cx="15" cy="15" r="13" fill="none" stroke="#a8adb4" stroke-width="1.3"/><path d="M15 8v14M8 15h14" stroke="#a8adb4" stroke-width="1.3"/></svg></div>
<div class="abs faq-row" style="top:1136px;height:59px"><span class="faq-q" style="top:19px">Lorem Ipsum is simply dummy text of the printing?</span>
  <svg class="faq-icon" style="top:16px" width="30" height="30" viewBox="0 0 30 30"><circle cx="15" cy="15" r="13" fill="none" stroke="#a8adb4" stroke-width="1.3"/><path d="M15 8v14M8 15h14" stroke="#a8adb4" stroke-width="1.3"/></svg></div>
<div class="abs faq-row" style="top:1195px;height:58px"><span class="faq-q" style="top:18px">Lorem Ipsum is simply dummy text of the printing ?</span>
  <svg class="faq-icon" style="top:14px" width="30" height="30" viewBox="0 0 30 30"><circle cx="15" cy="15" r="13" fill="none" stroke="#a8adb4" stroke-width="1.3"/><path d="M15 8v14M8 15h14" stroke="#a8adb4" stroke-width="1.3"/></svg></div>
<div class="abs faq-row" style="top:1253px;height:58px"><span class="faq-q" style="top:18px">Lorem Ipsum is simply dummy text of the printing and typesetting ?</span>
  <svg class="faq-icon" style="top:14px" width="30" height="30" viewBox="0 0 30 30"><circle cx="15" cy="15" r="13" fill="none" stroke="#a8adb4" stroke-width="1.3"/><path d="M15 8v14M8 15h14" stroke="#a8adb4" stroke-width="1.3"/></svg></div>
<div class="abs faq-row" style="top:1311px;height:58px"><span class="faq-q" style="top:18px">Lorem Ipsum is simply dummy text of the ?</span>
  <svg class="faq-icon" style="top:14px" width="30" height="30" viewBox="0 0 30 30"><circle cx="15" cy="15" r="13" fill="none" stroke="#a8adb4" stroke-width="1.3"/><path d="M15 8v14M8 15h14" stroke="#a8adb4" stroke-width="1.3"/></svg></div>
<div class="abs faq-row" style="top:1369px;height:68px"><span class="faq-q" style="top:18px">Lorem Ipsum is simply dummy text of the printing and typesetting ?</span>
  <svg class="faq-icon" style="top:17px" width="30" height="30" viewBox="0 0 30 30"><circle cx="15" cy="15" r="13" fill="none" stroke="#a8adb4" stroke-width="1.3"/><path d="M15 8v14M8 15h14" stroke="#a8adb4" stroke-width="1.3"/></svg></div>

<section class="abs blog"></section>
<h2 class="abs blog-title">Latest <b>Blog</b></h2>
<div class="abs search"><span>Search</span>
  <svg width="10" height="7" viewBox="0 0 10 7"><path d="M1 1l4 4 4-4" fill="none" stroke="#3a4250" stroke-width="1.2"/></svg></div>
<div class="abs blog-rule"></div>

<article class="abs card" style="left:151px;top:1715px"><span class="tag">BLOG</span><h3>Lorem Ipsum is simply dummy text of the</h3><p>Lorem Ipsum is simply dummy text of the printing and typesetting industry. Lorem Ipsum has been the industry's standard dummy text ever since the 1500s,</p><span class="go"><svg width="15" height="15" viewBox="0 0 15 15"><path d="M1 7.5h12M8 2.5l5 5-5 5" fill="none" stroke="#fff" stroke-width="1.4"/></svg></span></article>
<article class="abs card lift" style="left:460px;top:1715px"><span class="tag">BLOG</span><h3>Lorem Ipsum is simply dummy text of the</h3><p>Lorem Ipsum is simply dummy text of the printing and typesetting industry. Lorem Ipsum has been the industry's standard dummy text ever since the 1500s,</p><span class="go"><svg width="15" height="15" viewBox="0 0 15 15"><path d="M1 7.5h12M8 2.5l5 5-5 5" fill="none" stroke="#fff" stroke-width="1.4"/></svg></span></article>
<article class="abs card" style="left:768px;top:1715px"><span class="tag">BLOG</span><h3>Lorem Ipsum is simply dummy text of the</h3><p>Lorem Ipsum is simply dummy text of the printing and typesetting industry. Lorem Ipsum has been the industry's standard dummy text ever since the 1500s,</p><span class="go"><svg width="15" height="15" viewBox="0 0 15 15"><path d="M1 7.5h12M8 2.5l5 5-5 5" fill="none" stroke="#fff" stroke-width="1.4"/></svg></span></article>
<article class="abs card" style="left:151px;top:2021px"><span class="tag">BLOG</span><h3>Lorem Ipsum is simply dummy text of the</h3><p>Lorem Ipsum is simply dummy text of the printing and typesetting industry. Lorem Ipsum has been the industry's standard dummy text ever since the 1500s,</p><span class="go"><svg width="15" height="15" viewBox="0 0 15 15"><path d="M1 7.5h12M8 2.5l5 5-5 5" fill="none" stroke="#fff" stroke-width="1.4"/></svg></span></article>
<article class="abs card" style="left:460px;top:2021px"><span class="tag">BLOG</span><h3>Lorem Ipsum is simply dummy text of the</h3><p>Lorem Ipsum is simply dummy text of the printing and typesetting industry. Lorem Ipsum has been the industry's standard dummy text ever since the 1500s,</p><span class="go"><svg width="15" height="15" viewBox="0 0 15 15"><path d="M1 7.5h12M8 2.5l5 5-5 5" fill="none" stroke="#fff" stroke-width="1.4"/></svg></span></article>
<article class="abs card" style="left:768px;top:2021px"><span class="tag">BLOG</span><h3>Lorem Ipsum is simply dummy text of the</h3><p>Lorem Ipsum is simply dummy text of the printing and typesetting industry. Lorem Ipsum has been the industry's standard dummy text ever since the 1500s,</p><span class="go"><svg width="15" height="15" viewBox="0 0 15 15"><path d="M1 7.5h12M8 2.5l5 5-5 5" fill="none" stroke="#fff" stroke-width="1.4"/></svg></span></article>

<div class="abs more">More</div>

<div class="abs signup" style="left:364px;top:2485px;box-shadow:none">
  <span class="field">Your Email Address</span>
  <span class="btn">Subscribe</span>
</div>

<nav class="footer-nav">
  <a href="#" style="left:401px">Home</a>
  <a href="#" style="left:485px">Archive</a>
  <a href="#" style="left:579px">About</a>
</nav>
<svg class="abs social" style="left:712px" width="96" height="20" viewBox="0 0 96 20" role="img" aria-label="Social media links">
  <circle cx="8" cy="10" r="6" fill="none" stroke="#3a4250" stroke-width="1.5"/>
  <circle cx="40" cy="10" r="6" fill="none" stroke="#3a4250" stroke-width="1.5"/>
  <rect x="70" y="3" width="14" height="14" rx="3" fill="none" stroke="#3a4250" stroke-width="1.5"/>
</svg>
<div class="abs footer-rule"></div>
<p class="abs copy">Copyright 2021 Company Name</p>
<p class="abs legal" style="left:745px"><a href="#">Privacy Policy</a></p>
<p class="abs legal" style="left:876px">|</p>
<p class="abs legal" style="left:901px"><a href="#">Legal and Policies</a></p>

</body>
</html>
```